Torvel, Inc. new buisness cards - brand guide included

We need new business cards. SLEAK SIMPLE FINANCE. They must include a place for NAME, TITLE, CELL, OFFICE PHONE, EMAIL. they also must include our services across the bottom. AIR, OCEAN, FTL, LTL, EXPRESS. for reference this will be being handed to some of the most prestigious shipping companies in a america.

Target Market(s)

Finance and corporate

Contact Information for Business Card

We need new business cards. SLEAK SIMPLE FINANCE. They must include a place for NAME, TITLE, CELL, OFFICE PHONE, EMAIL. they also must include our services across the bottom. AIR, OCEAN, FTL, LTL, EXPRESS.

Requirements
Must have
• We need new business cards. SLEAK SIMPLE FINANCE. They must include a place for NAME, TITLE, CELL, OFFICE PHONE, EMAIL. they also must include our services across the bottom. AIR, OCEAN, FTL, LTL, EXPRESS.
Nice to have
• USE THE COLORS AND LOGO IN THE BRAND GUIDE :)

```html
<!DOCTYPE html>
<html lang="en">
<head>
<meta charset="utf-8">
<title>Torvel, Inc. Business Card</title>
<link rel="stylesheet" href="https://fonts.googleapis.com/css2?family=Tinos:wght@400;700&display=swap">
<style>
  :root {
    --stage: #161616;
    --card-dark: #2c2c2c;
    --card-dark-edge: #3a3a3a;
    --card-light: #ffffff;
    --ink: #1f1f1f;
    --ink-soft: #2e2e2e;
    --on-dark: #ffffff;
  }
  * { margin: 0; padding: 0; box-sizing: border-box; }
  html, body {
    width: 900px; height: 1200px; overflow: hidden;
    background: var(--stage);
    font-family: "Tinos", "Times New Roman", serif;
  }
  .canvas { position: relative; width: 900px; height: 1200px; }

  .card { position: absolute; left: 134px; width: 633px; height: 362px; }

  /* Front */
  .card-front { top: 212px; background: var(--card-dark); overflow: hidden; }
  .card-front .texture {
    position: absolute; inset: 0;
    background: linear-gradient(90deg, var(--card-dark) 0%, var(--card-dark) 45%, var(--card-dark-edge) 100%);
  }
  .card-front .brand-name {
    position: absolute; left: 0; right: 0; top: 150px;
    text-align: center; color: var(--on-dark);
    font-size: 56px; font-weight: 400; letter-spacing: 6px; line-height: 1;
  }

  /* Back */
  .card-back { top: 627px; background: var(--card-light); color: var(--ink); }
  .card-back .brand-name {
    position: absolute; left: 86px; top: 155px; width: 224px;
    text-align: center; font-size: 44px; letter-spacing: 4px; line-height: 1;
  }
  .divider {
    position: absolute; left: 342px; top: 82px; width: 1.5px; height: 197px;
    background: var(--ink);
  }
  .contact { position: absolute; left: 369px; top: 78px; }
  .contact .person-name { font-size: 24px; font-weight: 700; line-height: 1; }
  .contact .person-title { font-size: 15px; margin-top: 10px; line-height: 1; }
  .contact .address { font-size: 15px; line-height: 20px; margin-top: 13px; }
  .contact .lines { list-style: none; margin-top: 12px; }
  .contact .lines li {
    display: flex; align-items: center; gap: 7px;
    font-size: 14.5px; letter-spacing: 1px; height: 24.5px;
  }
  .contact .lines svg { width: 11px; height: 11px; fill: var(--ink-soft); flex: none; }
  .services {
    position: absolute; left: 0; right: 0; top: 313px;
    text-align: center; font-size: 18px; font-weight: 700; letter-spacing: 1.2px;
  }
</style>
</head>
<body>
<main class="canvas">
  <section class="card card-front">
    <div class="texture" role="img" aria-label="Dark embossed repeating brand-name pattern"></div>
    <div class="brand-name">TORVEL</div>
  </section>

  <section class="card card-back">
    <div class="brand-name">TORVEL</div>
    <div class="divider"></div>
    <div class="contact">
      <div class="person-name">Dorian Vale</div>
      <div class="person-title">CEO</div>
      <div class="address">2810 Harbor Pointe Dr Ste 410<br>Larkfield, WA 98111</div>
      <ul class="lines">
        <li><svg viewBox="0 0 12 12"><path d="M3 0h6a1 1 0 0 1 1 1v10a1 1 0 0 1-1 1H3a1 1 0 0 1-1-1V1a1 1 0 0 1 1-1zm0 1.5v8h6v-8zM6 10.2a.6.6 0 1 0 0 1.2.6.6 0 0 0 0-1.2z"/></svg>555-201-4837</li>
        <li><svg viewBox="0 0 12 12"><path d="M2.4 0.6l1.8 2.6-1.1 1.3a7 7 0 0 0 4.4 4.4l1.3-1.1 2.6 1.8-1 2A2 2 0 0 1 8.3 12 9 9 0 0 1 0 3.7a2 2 0 0 1 .4-2.1z"/></svg>555-308-6190</li>
        <li><svg viewBox="0 0 12 12"><path d="M0 2h12v1L6 7 0 3zM0 4.3l6 4 6-4V10H0z"/></svg>hello@torvelinc.com</li>
        <li><svg viewBox="0 0 12 12"><path d="M6 0a6 6 0 1 0 0 12A6 6 0 0 0 6 0zm4.4 5.3H8.3a9 9 0 0 0-.8-3.6 4.6 4.6 0 0 1 2.9 3.6zM6 1.3c.6.8 1 2.3 1.1 4H4.9c.1-1.7.5-3.2 1.1-4zM4.5 1.7a9 9 0 0 0-.8 3.6H1.6a4.6 4.6 0 0 1 2.9-3.6zM1.6 6.7h2.1a9 9 0 0 0 .8 3.6 4.6 4.6 0 0 1-2.9-3.6zM6 10.7c-.6-.8-1-2.3-1.1-4h2.2c-.1 1.7-.5 3.2-1.1 4zm1.5-.4a9 9 0 0 0 .8-3.6h2.1a4.6 4.6 0 0 1-2.9 3.6z"/></svg>www.torvelinc.com</li>
      </ul>
    </div>
    <div class="services">AIR | OCEAN | FTL | LTL | EXPRESS.</div>
  </section>
</main>
</body>
</html>
```